Design a small family icons for Wextra

I need a family of seven icons to be designed for a website:

The seven icons need to represent:

1. Business Improvement
2. Marketing
3. Accounting and Compliance
4. Stock levels and supply chain
5. Store of the future
6. Open API
7. Data sharing

I have attached Wextra's logo to give a feel for the brand and also a video about the product can be seen here:

www.vidloom-example.com/watch?v=kRt4Pq8zLm2

Target Market(s)

Business owners

Industry/Entity Type

Business

Requirements
Must have
• Creative yet clear icons for a website
• Colors to match the logo
Nice to have
• Consistent themes between the icons
• The icons can either be buttonised squares, circles or spheres
Should not have
• Overly busy icons

```html
<!DOCTYPE html>
<html lang="en">
<head>
<meta charset="utf-8">
<title>Wextra Services</title>
<link rel="stylesheet" href="https://fonts.googleapis.com/css2?family=Questrial&display=swap">
<style>
  :root {
    --brand-green: #0a9647;
    --icon-line: #ffffff;
    --label-grey: #7a7a7a;
    --page-bg: #ffffff;
    --hero-dark: #232323;
    --hero-mid: #3c3c3c;
    --hero-light: #8a8a8a;
  }
  * { margin: 0; padding: 0; box-sizing: border-box; }
  html, body {
    width: 1200px;
    height: 857px;
    overflow: hidden;
    background: var(--page-bg);
    font-family: "Questrial", "Helvetica Neue", Arial, sans-serif;
  }
  .page { position: relative; width: 1200px; height: 857px; }
  .hero {
    position: absolute; left: 0; top: 0; width: 1200px; height: 314px;
    background:
      radial-gradient(ellipse 420px 200px at 260px 90px, rgba(200,200,200,0.55), transparent 70%),
      linear-gradient(180deg, var(--hero-light) 0%, var(--hero-mid) 35%, var(--hero-dark) 100%);
  }
  .service {
    position: absolute; width: 300px; margin-left: -150px;
    text-align: center;
  }
  .service-badge {
    display: block; width: 78px; height: 78px; margin: 0 auto;
    border-radius: 50%; background: var(--brand-green);
  }
  .service-badge svg { width: 78px; height: 78px; display: block; }
  .service-badge svg * {
    fill: none; stroke: var(--icon-line); stroke-width: 1.6;
    stroke-linecap: round; stroke-linejoin: round;
  }
  .service-name {
    display: block; margin-top: 24px;
    font-size: 18px; letter-spacing: 0.4px; color: var(--label-grey);
  }
  .badge-text { fill: var(--icon-line) !important; stroke: none !important;
    font-family: "Questrial", Arial, sans-serif; font-size: 15px; }
</style>
</head>
<body>
<main class="page">
  <div class="hero" role="img" aria-label="Photo of a laptop, smartphone and pen on a dark desk"></div>

  <section class="service" style="left:313px; top:353px;">
    <span class="service-badge"><svg viewBox="0 0 78 78">
      <path d="M24 28 L50 54 M27 24 L24 28 L20 25 L26 20 L32 23 Z"/>
      <path d="M52 23 a7 7 0 0 0 -8 9 L26 50 a3 3 0 0 0 4 4 L48 36 a7 7 0 0 0 9 -8 l-4 4 -4 -1 -1 -4 z"/>
    </svg></span>
    <span class="service-name">Business Improvement</span>
  </section>

  <section class="service" style="left:596px; top:353px;">
    <span class="service-badge"><svg viewBox="0 0 78 78">
      <rect x="20" y="44" width="6" height="14"/><rect x="30" y="38" width="6" height="20"/>
      <rect x="40" y="41" width="6" height="17"/><rect x="50" y="30" width="6" height="28"/>
      <path d="M18 60 H60 M22 38 L33 28 L43 34 L56 18 M51 18 H56 V23"/>
    </svg></span>
    <span class="service-name">Marketing</span>
  </section>

  <section class="service" style="left:884px; top:353px;">
    <span class="service-badge"><svg viewBox="0 0 78 78">
      <rect x="24" y="17" width="30" height="44" rx="2"/>
      <rect x="28" y="21" width="22" height="7"/>
      <path d="M28 33 h4 v4 h-4 z M34 33 h4 v4 h-4 z M40 33 h4 v4 h-4 z M46 33 h4 v4 h-4 z
               M28 40 h4 v4 h-4 z M34 40 h4 v4 h-4 z M40 40 h4 v4 h-4 z M46 40 h4 v4 h-4 z
               M28 47 h4 v4 h-4 z M34 47 h4 v4 h-4 z M40 47 h4 v4 h-4 z M46 47 h4 v4 h-4 z
               M28 54 h4 v4 h-4 z M34 54 h4 v4 h-4 z M40 54 h10 v4 h-10 z"/>
    </svg></span>
    <span class="service-name">Accounting &amp; Compliance</span>
  </section>

  <section class="service" style="left:313px; top:524px;">
    <span class="service-badge"><svg viewBox="0 0 78 78">
      <path d="M54 20 C44 20 34 28 28 40 L36 48 C48 42 56 32 56 22 Z"/>
      <circle cx="46" cy="30" r="3"/><circle cx="40" cy="36" r="2"/>
      <path d="M30 38 L22 40 L18 46 L26 45 M38 48 L36 56 L30 60 L31 52 M28 48 L20 58 M24 44 L18 52"/>
    </svg></span>
    <span class="service-name">Store of the Future</span>
  </section>

  <section class="service" style="left:596px; top:524px;">
    <span class="service-badge"><svg viewBox="0 0 78 78">
      <path d="M30 18 h18 M34 14 v8 h4 v-5 h4 v5 M39 22 v8 M22 36 v-6 h34 v6"/>
      <rect x="27" y="34" width="24" height="16" rx="1"/>
      <path d="M35 54 h8 M39 50 v4"/>
      <rect x="15" y="38" width="6" height="12"/><rect x="57" y="36" width="8" height="14"/>
    </svg></span>
    <span class="service-name">Data Sharing</span>
  </section>

  <section class="service" style="left:884px; top:524px;">
    <span class="service-badge"><svg viewBox="0 0 78 78">
      <circle cx="39" cy="40" r="17"/>
      <ellipse cx="39" cy="40" rx="7" ry="17"/>
      <path d="M22 40 H56 M25 31 H53 M25 49 H53 M39 23 V57"/>
      <path d="M30 15 a26 26 0 0 1 20 0 M30 15 l3 -3 M30 15 l4 2"/>
      <path d="M15 46 a26 26 0 0 0 6 12 M21 58 v-4"/>
      <path d="M63 46 a26 26 0 0 1 -6 12 M63 46 l-3 3 M63 46 l2 4"/>
    </svg></span>
    <span class="service-name">Open API</span>
  </section>

  <section class="service" style="left:596px; top:698px;">
    <span class="service-badge"><svg viewBox="0 0 78 78">
      <path d="M18 38 L27 30 L35 37 L52 20 M45 20 H52 V27" style="stroke-width:3"/>
      <path d="M14 60 L18 54 L22 60 Z" style="fill:#fff"/>
      <text class="badge-text" x="24" y="61">+5.44</text>
    </svg></span>
    <span class="service-name">Stock Levels &amp; Supply Chain</span>
  </section>
</main>
</body>
</html>
```